Childrens Business Card Design Project

We have an existing logo attached which we'd like to use as part of our new business card design.

The design needs to be relatively gender neutral and contain bright colours.

In terms of look and feel think:

Fun, Modern, Quality (as opposed to cheap!) and of course Party!

Single or double sided - i am not decided on either one yet - ideally i'd like to see designs for both because if you think stylistically it would benefit having two sides then please try it out!

I think the challenge here is finding a really good background colour (if you think it needs one) and also choosing an eye grabbing text that compliments the existing logo - do that an you are onto a winner! I have another image for the business (which i have attached) which uses stripes so i am keen to see a design that incorporates this to tie in all my collateral.

The copy required is as follows (not necesarily in this order)

Bookings/Enquiries:

Tilda

T: 0498 217 503
E: enquiries@brightfoxparties.example.au

ABN: 47 302 658 114

Any feedback on text is welcomed - please message me or add to the discussion.

Reason: Hi All, I have received some promising designs, but overall i am not impressed with the quality of the work so have extended the deadline as this project has been committed. I will aim to attach some business card examples to the brief tomorrow to give further guidance as a whole but please do not submit any designs on a generic background that are not related to the theme, have been carelessly placed with overlapping elements - it just looks sloppy. For those who have read the brief an incorporated stripes or even spots this is on target as it convey's a party theme, however please work on getting the colours for the contact details by either a bold solid strip to highlight or some other way to frame it. When it comes to the logo, some people have removed the characters all together and changed the colour of the wording - this is fine. Also feel free to balloons starts - but keep it classy and watch your placement of these. I hope this helps and for the designs i would like to see revisions for i will aim to get back to you individually over the next day or so. Many thanks all.

Target Market(s)

Mothers in the suburbs of Australia with a disposal able income, children aged between 1-7 years old.

Industry/Entity Type

Business

Requirements
Must have
• The font and wording positioning must compliment the logo.

```html
<!DOCTYPE html>
<html lang="en">
<head>
<meta charset="utf-8">
<title>Bright Fox – Business Card</title>
<link rel="stylesheet" href="https://fonts.googleapis.com/css2?family=Cinzel:wght@700;900&display=swap">
<style>
  :root {
    --stripe-mint: #ccf9d6;
    --stripe-white: #ffffff;
    --ink: #111111;
    --brand-blue: #3db3ee;
    --tag-orange: #f59a5a;
    --fairy-pink: #f7a1c4;
    --fairy-wing: #a8f0c4;
    --clown-orange: #f8a63a;
    --clown-yellow: #f4e64a;
    --pirate-blue: #5aa7ef;
    --pirate-red: #ee3a3a;
  }
  html, body {
    margin: 0;
    padding: 0;
    width: 1200px;
    height: 702px;
    overflow: hidden;
    background: #ffffff;
  }
  .card {
    position: relative;
    width: 1200px;
    height: 702px;
    overflow: hidden;
    background: repeating-linear-gradient(
      to right,
      var(--stripe-mint) 0 25px,
      var(--stripe-white) 25px 50px
    );
    font-family: "Cinzel", "Times New Roman", serif;
    color: var(--ink);
  }
  .character {
    position: absolute;
    border-radius: 40% 40% 30% 30%;
  }
  .character--fairy {
    left: 188px; top: 139px; width: 176px; height: 180px;
    background: linear-gradient(160deg, var(--fairy-wing), var(--fairy-pink) 60%, #f26b9c);
  }
  .character--clown {
    left: 536px; top: 89px; width: 168px; height: 225px;
    background: linear-gradient(180deg, var(--clown-orange), var(--clown-yellow) 55%, #7ad84a);
  }
  .character--pirate {
    left: 830px; top: 167px; width: 220px; height: 150px;
    background: linear-gradient(200deg, var(--pirate-red), var(--pirate-blue) 50%, #6b4a2e);
  }
  .brand {
    position: absolute;
    left: 0; right: 0;
    top: 338px;
    text-align: center;
  }
  .brand__name {
    margin: 0;
    font-weight: 700;
    font-size: 84px;
    line-height: 1;
    letter-spacing: 6px;
    color: var(--brand-blue);
  }
  .brand__tagline {
    margin: 16px 0 0;
    font-weight: 700;
    font-size: 20px;
    letter-spacing: 2px;
    color: var(--tag-orange);
  }
  .contact {
    position: absolute;
    margin: 0;
    font-weight: 900;
    font-size: 25px;
    line-height: 34px;
    text-transform: uppercase;
    white-space: nowrap;
  }
  .contact--bookings {
    left: 73px; top: 540px;
  }
  .contact--email {
    right: 70px; top: 540px;
    text-align: right;
  }
  .contact--abn {
    right: 70px; top: 606px;
    text-align: right;
  }
  .contact p { margin: 0; }
</style>
</head>
<body>
  <div class="card">
    <div class="character character--fairy" role="img" aria-label="Illustration of a smiling fairy child in a pink dress with wand and green wings"></div>
    <div class="character character--clown" role="img" aria-label="Illustration of a clown in a polka-dot suit doing a handstand"></div>
    <div class="character character--pirate" role="img" aria-label="Illustration of a pirate child with red bandana, eye patch and sword"></div>

    <div class="brand">
      <h1 class="brand__name">Bright Fox</h1>
      <p class="brand__tagline">Kids Parties &amp; Events</p>
    </div>

    <div class="contact contact--bookings">
      <p>Bookings/Enquiries:</p>
      <p>Tilda</p>
      <p>T: 0498 217 503</p>
    </div>
    <div class="contact contact--email">
      <p>E: enquiries@brightfoxparties.example.au</p>
    </div>
    <div class="contact contact--abn">
      <p>ABN: 47 302 658 114</p>
    </div>
  </div>
</body>
</html>
```